Brindle Cyto company values interaction - arch and foundation

We need a graphic that represents the relationship between our company's values. Our company, Brindle Cyto, is a biotechnology startup based in Seattle. We are pushing the boundaries of biology to create tailored cell therapy solutions through protein design and custom programming to cure diseases. Our values are Respect, Inclusion, Science, Innovation and Collaboration. We view Respect and Inclusion as the foundation on which our other values rest, with Science and Collaboration supporting Innovation. We have styled this as an arch with Innovation in the middle (see attached file). We would like to show this graphic on our careers page to help candidates know what we're all about. See: https://www.brindlecyto.example/careers

Target Market(s)

Potential job applicants, current employees and anyone who wants to know what we're about

Industry/Entity Type

Biotechnology

Font styles to use
Sans Serif

Colors

Designer to choose colors to be used in the design.

Requirements
Must have
• A foundation that supports an arch to demonstrate how our values drive our culture and mission

```html
<!DOCTYPE html>
<html lang="en">
<head>
<meta charset="utf-8">
<title>Brindle Cyto – Company Values</title>
<link rel="stylesheet" href="https://fonts.googleapis.com/css2?family=Barlow+Semi+Condensed:wght@500;600&family=Jost:wght@300;400&display=swap">
<style>
  :root {
    --bg: #1166a8;
    --white: #ffffff;
    --science-top: #4fb868;
    --science-bottom: #0a9a45;
    --innovation-top: #a072b9;
    --innovation-bottom: #74298d;
    --collab-top: #45c6f2;
    --collab-bottom: #0aa0df;
    --respect-top: #d60f8a;
    --respect-bottom: #f04fa8;
    --inclusion-top: #df2c4d;
    --inclusion-bottom: #f47f76;
  }
  html, body {
    margin: 0;
    padding: 0;
    width: 1200px;
    height: 1200px;
    overflow: hidden;
    background: var(--bg);
  }
  .values-graphic {
    display: block;
    width: 1200px;
    height: 1200px;
    background: var(--bg);
  }
  .value-tile {
    stroke: var(--white);
    stroke-width: 4;
  }
  .value-label {
    font-family: "Barlow Semi Condensed", "Arial Narrow", sans-serif;
    font-weight: 600;
    font-size: 35px;
    fill: var(--white);
    text-anchor: middle;
  }
  .value-icon {
    fill: none;
    stroke: var(--white);
    stroke-width: 2.4;
    stroke-linecap: round;
    stroke-linejoin: round;
  }
  .flow-arrow {
    fill: none;
    stroke: var(--white);
    stroke-width: 2.2;
  }
  .flow-dot { fill: var(--white); }
  .brand-name {
    font-family: "Jost", sans-serif;
    font-weight: 400;
    font-size: 54px;
    letter-spacing: 4px;
    fill: var(--white);
    text-anchor: middle;
  }
  .brand-tagline {
    font-family: "Jost", sans-serif;
    font-weight: 400;
    font-size: 27px;
    letter-spacing: 2.5px;
    fill: var(--white);
    text-anchor: middle;
  }
</style>
</head>
<body>
<svg class="values-graphic" viewBox="0 0 1000 1000" xmlns="http://www.w3.org/2000/svg" role="img" aria-label="Brindle Cyto company values: Science, Innovation and Collaboration form an arch resting on Respect and Inclusion">
  <defs>
    <linearGradient id="grad-science" x1="0" y1="0" x2="0" y2="1">
      <stop offset="0" stop-color="var(--science-top)"/><stop offset="0.5" stop-color="var(--science-bottom)"/>
    </linearGradient>
    <linearGradient id="grad-innovation" x1="0" y1="0" x2="0" y2="1">
      <stop offset="0" stop-color="var(--innovation-top)"/><stop offset="0.6" stop-color="var(--innovation-bottom)"/>
    </linearGradient>
    <linearGradient id="grad-collab" x1="0" y1="0" x2="0" y2="1">
      <stop offset="0" stop-color="var(--collab-top)"/><stop offset="0.6" stop-color="var(--collab-bottom)"/>
    </linearGradient>
    <linearGradient id="grad-respect" x1="0" y1="0" x2="0" y2="1">
      <stop offset="0.4" stop-color="var(--respect-top)"/><stop offset="1" stop-color="var(--respect-bottom)"/>
    </linearGradient>
    <linearGradient id="grad-inclusion" x1="0" y1="0" x2="0" y2="1">
      <stop offset="0.3" stop-color="var(--inclusion-top)"/><stop offset="1" stop-color="var(--inclusion-bottom)"/>
    </linearGradient>
    <marker id="arrowhead" viewBox="0 0 10 10" refX="8" refY="5" markerWidth="7" markerHeight="7" orient="auto-start-reverse" markerUnits="userSpaceOnUse">
      <path d="M1,1 L8,5 L1,9" fill="none" stroke="#fff" stroke-width="1.8"/>
    </marker>
  </defs>

  <!-- flow arrows, arch -->
  <g class="flow-arrows">
    <circle class="flow-dot" cx="48" cy="290" r="7"/>
    <path class="flow-arrow" d="M48,290 A150,112 0 0 1 342,290" marker-end="url(#arrowhead)"/>
    <path class="flow-arrow" d="M358,290 A143,112 0 0 1 643,290" marker-start="url(#arrowhead)" marker-end="url(#arrowhead)"/>
    <circle class="flow-dot" cx="950" cy="290" r="7"/>
    <path class="flow-arrow" d="M950,290 A146,112 0 0 0 658,290" marker-end="url(#arrowhead)"/>
  </g>

  <!-- flow arrows, foundation -->
  <g class="flow-arrows">
    <circle class="flow-dot" cx="492" cy="577" r="7"/>
    <path class="flow-arrow" d="M492,577 A144,108 0 0 1 206,578" marker-end="url(#arrowhead)"/>
    <circle class="flow-dot" cx="521" cy="577" r="7"/>
    <path class="flow-arrow" d="M521,577 A144,108 0 0 0 808,578" marker-end="url(#arrowhead)"/>
  </g>

  <!-- arch values -->
  <g class="value value-science">
    <path class="value-tile" fill="url(#grad-science)" d="M62,332 L152,242 Q202,192 252,242 L342,332 L202,472 Z"/>
    <text class="value-label" x="202" y="344">Science</text>
    <g class="value-icon" transform="translate(202,388)">
      <path d="M-14,-26 L-14,-8 L-30,20 Q-32,26 -26,26 L0,26 Q6,26 4,20 L-10,-8 L-10,-26 Z"/>
      <line x1="-17" y1="-26" x2="-7" y2="-26"/>
      <path d="M-24,12 L-2,12"/>
      <circle cx="16" cy="12" r="14"/>
      <path d="M12,-2 L12,-18 L20,-18 L20,-2"/>
      <path d="M4,12 L28,12"/>
    </g>
  </g>

  <g class="value value-innovation">
    <path class="value-tile" fill="url(#grad-innovation)" d="M362,332 L451,242 Q501,192 551,242 L640,332 L501,472 Z"/>
    <text class="value-label" x="501" y="344">Innovation</text>
    <g class="value-icon" transform="translate(501,385)">
      <path d="M-10,18 Q-10,8 -16,2 A20,20 0 1 1 16,2 Q10,8 10,18 Z"/>
      <line x1="-9" y1="24" x2="9" y2="24"/>
      <line x1="-6" y1="30" x2="6" y2="30"/>
      <circle cx="0" cy="-10" r="7"/>
      <path d="M0,-21 V-19 M0,-1 V1 M-11,-10 H-9 M9,-10 H11"/>
      <path d="M0,-36 V-30 M-22,-26 L-18,-22 M22,-26 L18,-22 M-30,-8 H-25 M30,-8 H25"/>
    </g>
  </g>

  <g class="value value-collaboration">
    <path class="value-tile" fill="url(#grad-collab)" d="M659,332 L749,242 Q799,192 849,242 L939,332 L799,472 Z"/>
    <text class="value-label" x="799" y="344">Collaboration</text>
    <g class="value-icon" transform="translate(799,392)">
      <path d="M-28,26 L-14,8 Q-10,-4 0,-8 L10,-12"/>
      <path d="M28,26 L14,8 Q10,-4 0,-8"/>
      <path d="M-8,-2 Q0,-16 10,-10 Q16,-4 8,6 Q0,10 -6,4"/>
      <path d="M-34,20 L-22,32 M34,20 L22,32"/>
      <path d="M-12,-30 L-8,-22 M0,-34 V-24 M12,-30 L8,-22"/>
    </g>
  </g>

  <!-- foundation values -->
  <g class="value value-respect">
    <path class="value-tile" fill="url(#grad-respect)" d="M220,530 L359,391 L498,530 L409,619 Q359,669 309,619 Z"/>
    <text class="value-label" x="359" y="548">Respect</text>
    <g class="value-icon" transform="translate(359,470)">
      <rect x="-30" y="-6" width="12" height="30"/>
      <path d="M-18,-4 L-6,-10 L0,-28 Q6,-32 8,-24 L6,-10 L26,-10 Q32,-8 30,-2 L26,18 Q24,24 18,24 L-18,22"/>
      <path d="M6,-36 L10,-44 M16,-32 L24,-38 M20,-24 L28,-26"/>
    </g>
  </g>

  <g class="value value-inclusion">
    <path class="value-tile" fill="url(#grad-inclusion)" d="M521,530 L660,391 L799,530 L710,619 Q660,669 610,619 Z"/>
    <text class="value-label" x="660" y="548">Inclusion</text>
    <g class="value-icon" transform="translate(660,468)">
      <path d="M-36,-14 L-14,-8 L8,-18 L20,-16"/>
      <path d="M36,-14 L14,-8 L-6,2"/>
      <path d="M-10,-30 L-10,-4 M0,-4 L0,26"/>
      <path d="M-14,4 L14,4 L14,14 L-14,14 Z"/>
      <rect x="-8" y="28" width="16" height="8"/>
      <rect x="-44" y="-20" width="8" height="14"/>
      <rect x="36" y="-20" width="8" height="14"/>
      <rect x="-14" y="-40" width="8" height="10"/>
    </g>
  </g>

  <!-- brand -->
  <text class="brand-name" x="500" y="848">BRINDLE CYTO</text>
  <text class="brand-tagline" x="500" y="914">COMPANY VALUES</text>
</svg>
</body>
</html>
```